physical therapy flyer

2 office locations speciality programs - work injury / Motor vehicle accidents - spanish speaking - do not put balance defecits/ fall prevention - Spanish speaking
neck and back pain shoulder pain/ rotator cuff disorder / bursitis
hip pain knee andle and foot pain post operative care including Spine , shoulder , knee , total joint replacement

Meadowlark Physical therapy & Chiropractic
4827 Ashbury BLvd
lindell park ny 11592
7185528174
3719 Tillman Parkway
Corvale NY 11592
7182947061
www.meadowlarkptchiroacu.com

```html
<!DOCTYPE html>
<html lang="en">
<head>
<meta charset="utf-8">
<title>Meadowlark Physical Therapy Flyer</title>
<link href="https://fonts.googleapis.com/css2?family=Poppins:wght@400;500;600;700;800&display=swap" rel="stylesheet">
<style>
  :root {
    --green: #34a33c;
    --green-light: #5cb83a;
    --green-dark: #2b9a36;
    --ink: #2a2a2a;
    --paper: #f3f3f1;
    --stage: #a3b8b8;
    --white: #ffffff;
  }
  * { margin: 0; padding: 0; box-sizing: border-box; }
  html, body { width: 1200px; height: 1117px; overflow: hidden; }
  body {
    background: var(--stage);
    font-family: "Poppins", sans-serif;
    position: relative;
  }
  .flyer {
    position: absolute;
    left: 219px; top: 18px;
    width: 762px; height: 1080px;
    background: var(--paper);
    overflow: hidden;
  }
  .hero-photo {
    position: absolute; left: 370px; top: 0; width: 392px; height: 287px;
    background: linear-gradient(135deg, #eceae6 0%, #e3ddd6 50%, #d9cfc4 100%);
  }
  .hero-shape { position: absolute; left: 0; top: 0; }
  .brand {
    position: absolute; left: 60px; top: 52px;
    display: flex; align-items: center; gap: 10px;
  }
  .brand-dot { width: 34px; height: 34px; border-radius: 50%; background: var(--green); }
  .brand-name {
    color: var(--green); font-weight: 400; font-size: 15px; line-height: 18px;
  }
  .headline {
    position: absolute; left: 20px; width: 340px; top: 160px;
    text-align: center; color: var(--white);
    font-weight: 800; font-size: 46px; line-height: 44px; letter-spacing: -0.5px;
  }
  .photo-circle {
    position: absolute; border-radius: 50%;
  }
  .photo-exercise {
    left: 31px; top: 316px; width: 340px; height: 340px;
    background: radial-gradient(circle at 55% 45%, #9aa7b3 0%, #5f7182 55%, #d6dade 100%);
  }
  .photo-neck {
    left: 123px; top: 527px; width: 252px; height: 252px;
    border: 6px solid var(--paper);
    background: radial-gradient(circle at 45% 50%, #c7a48c 0%, #d9d9d9 55%, #eeeeee 100%);
  }
  .count {
    position: absolute; left: 378px; top: 300px;
    font-size: 72px; font-weight: 700; color: var(--green); line-height: 1;
  }
  .count-label {
    position: absolute; left: 438px; top: 322px;
    font-size: 20px; font-weight: 700; color: var(--green); line-height: 25px;
  }
  .programs { position: absolute; left: 416px; top: 392px; width: 320px; list-style: none; }
  .programs li {
    position: absolute; left: 0; width: 320px;
    padding-left: 27px; font-size: 16.5px; line-height: 20px; color: var(--ink);
  }
  .programs svg { position: absolute; left: 0; top: 4px; }
  .footer-band {
    position: absolute; left: 0; top: 790px; width: 762px; height: 218px;
    background: var(--green-dark);
  }
  .footer-title {
    position: absolute; left: 75px; top: 31px; width: 612px; height: 52px;
    border: 3px solid var(--white); border-radius: 8px;
    color: var(--white); font-weight: 700; font-size: 22px;
    display: flex; align-items: center; justify-content: center;
  }
  .office {
    position: absolute; top: 102px; color: var(--white);
    font-weight: 500; font-size: 18.5px; line-height: 24px;
  }
  .office-left { left: 83px; }
  .office-right { left: 414px; }
  .office-row { display: flex; gap: 9px; align-items: flex-start; }
  .office-row + .office-row { margin-top: 14px; }
  .office-row svg { flex: none; margin-top: 3px; }
  .divider {
    position: absolute; left: 379px; top: 98px; width: 1px; height: 90px;
    background: #a6cf4a;
  }
  .website {
    position: absolute; left: 0; top: 1026px; width: 762px; text-align: center;
    font-weight: 700; font-size: 23px; color: var(--ink);
  }
</style>
</head>
<body>
  <main class="flyer">
    <div class="hero-photo" role="img" aria-label="Clinician in a white coat explaining a spine model to a patient"></div>
    <svg class="hero-shape" width="762" height="400" viewBox="0 0 762 400" aria-hidden="true">
      <defs>
        <linearGradient id="greenFill" x1="0" y1="0" x2="1" y2="1">
          <stop offset="0" stop-color="#45ab3a"/>
          <stop offset="1" stop-color="#62b936"/>
        </linearGradient>
      </defs>
      <path d="M0,98 Q200,190 404,62 C432,180 392,300 280,336 Q190,345 120,334 C60,322 20,304 0,292 Z"
            fill="url(#greenFill)" stroke="#ffffff" stroke-width="6"/>
    </svg>

    <div class="brand">
      <span class="brand-dot"></span>
      <span class="brand-name">Meadowlark Physical Therapy,<br>Chiropractic, and Acupuncture</span>
    </div>

    <h1 class="headline">WE CREATE<br>HEALTHY<br>FAMILIES</h1>

    <div class="photo-circle photo-exercise" role="img" aria-label="Therapist guiding an older man through a stretching exercise"></div>
    <div class="photo-circle photo-neck" role="img" aria-label="Chiropractor adjusting a patient's neck"></div>

    <div class="count">2</div>
    <div class="count-label">OFFICE LOCATIONS<br>SPECIALITY PROGRAMS</div>

    <ul class="programs">
      <li style="top:0"><svg width="16" height="13" viewBox="0 0 16 13"><path d="M1,7 L6,11 L15,1" fill="none" stroke="#34a33c" stroke-width="3"/></svg>work injury / Motor vehicle<br>accidents -</li>
      <li style="top:61px"><svg width="16" height="13" viewBox="0 0 16 13"><path d="M1,7 L6,11 L15,1" fill="none" stroke="#34a33c" stroke-width="3"/></svg>do not put balance defecits/<br>fall prevention</li>
      <li style="top:122px"><svg width="16" height="13" viewBox="0 0 16 13"><path d="M1,7 L6,11 L15,1" fill="none" stroke="#34a33c" stroke-width="3"/></svg>neck and back pain</li>
      <li style="top:163px"><svg width="16" height="13" viewBox="0 0 16 13"><path d="M1,7 L6,11 L15,1" fill="none" stroke="#34a33c" stroke-width="3"/></svg>shoulder pain / rotator cuff</li>
      <li style="top:204px"><svg width="16" height="13" viewBox="0 0 16 13"><path d="M1,7 L6,11 L15,1" fill="none" stroke="#34a33c" stroke-width="3"/></svg>disorder / bursitis</li>
      <li style="top:244px"><svg width="16" height="13" viewBox="0 0 16 13"><path d="M1,7 L6,11 L15,1" fill="none" stroke="#34a33c" stroke-width="3"/></svg>hip pain knee andle and<br>foot pain post operative care<br>including Spine , shoulder ,<br>knee , total joint replacement</li>
      <li style="top:345px"><svg width="16" height="13" viewBox="0 0 16 13"><path d="M1,7 L6,11 L15,1" fill="none" stroke="#34a33c" stroke-width="3"/></svg>spanish speaking</li>
    </ul>

    <section class="footer-band">
      <div class="footer-title">Meadowlark Physical therapy &amp; Chiropractic</div>
      <div class="office office-left">
        <div class="office-row">
          <svg width="16" height="20" viewBox="0 0 16 20"><path d="M8,0 C3.6,0 0,3.5 0,7.8 C0,13 8,20 8,20 C8,20 16,13 16,7.8 C16,3.5 12.4,0 8,0 Z" fill="#fff"/><circle cx="8" cy="7.6" r="3" fill="#2b9a36"/></svg>
          <span>4827 Ashbury BLvd<br>lindell park ny 11592</span>
        </div>
        <div class="office-row">
          <svg width="18" height="18" viewBox="0 0 18 18"><circle cx="9" cy="9" r="9" fill="#fff"/><path d="M5.5,4.5 L7.5,4.3 L8.3,6.8 L7.1,7.8 C7.8,9.3 8.8,10.3 10.2,11 L11.2,9.8 L13.7,10.6 L13.5,12.6 C9,13 5,9 5.5,4.5 Z" fill="#2b9a36"/></svg>
          <span>7185528174</span>
        </div>
      </div>
      <div class="divider"></div>
      <div class="office office-right">
        <div class="office-row">
          <svg width="16" height="20" viewBox="0 0 16 20"><path d="M8,0 C3.6,0 0,3.5 0,7.8 C0,13 8,20 8,20 C8,20 16,13 16,7.8 C16,3.5 12.4,0 8,0 Z" fill="#fff"/><circle cx="8" cy="7.6" r="3" fill="#2b9a36"/></svg>
          <span>3719 Tillman Parkway<br>Corvale NY 11592</span>
        </div>
        <div class="office-row">
          <svg width="18" height="18" viewBox="0 0 18 18"><circle cx="9" cy="9" r="9" fill="#fff"/><path d="M5.5,4.5 L7.5,4.3 L8.3,6.8 L7.1,7.8 C7.8,9.3 8.8,10.3 10.2,11 L11.2,9.8 L13.7,10.6 L13.5,12.6 C9,13 5,9 5.5,4.5 Z" fill="#2b9a36"/></svg>
          <span>7182947061</span>
        </div>
      </div>
    </section>

    <div class="website">www.meadowlarkptchiroacu.com</div>
  </main>
</body>
</html>
```